Professional and modern website for Real Estate services company

Hi there! We're looking for a responsive, highly professional and modern (in line with Latest trends) coded website for a Real Estate services company named Portalia (find logo attached). I will try to Explain how I picture it in my head, but feel free to step out of the script and design it as you please. The structure for the website must be as Follows: - Menu: at the top of the screen, always visible (in any page and when to scrolling down). Logo at the left hand side (clicking redirects to home), then a Services, About us, Blog and Contact and on the right hand, Estimate and Log in (just placeholder, no log in required yet). - Home: (I like https://fr.domvera.example/): a landscape picture of Madrid's skyline. Very important That at a first glance (without scrolling) you can see a box to input data of your building to get an estimate (Post code, Number of homes, Number of garages, Number of stores, Swimming pool (yes / no) Concierge (yes / no)). Should there be a small space Also for a corporate presentation video (more or less like https://www.velbrastahogares.example/ but With the estimate Request box INSTEAD OF the App - however, do not take this one as example Given I just wanted to illustrate the structure). Still in the Home, bellow the first glance, I'd like to have a brief introduction of the following pages (Services, About us, Blog and Contact). This can be in a Either "square" form (like https://fr.domvera.example/) or in a "scroll" form (like https://k7pisos.example/). - Services: we offer 3 sets of services, each of them composed by three specific services, Namely: * Administration Treasury Accounting Savings * Consulting Legal Technical Regulatory * Mediation Repairs Meetings Delinquency For the sake of structuring, each of the nine services will Have to written description composed of 3 small paragraphs of About 15 words. I Tend to like to Accompany With each of the services related icons / vectors, but feel free to design them as you want. - About us: content not yet defined, but will be a series of bullets / sections in Which We talk about prep or differentiating points. We can include the corporate video presentation here again. - Blog: just a space Where you can see to the blog entries (in Home, probably just show 3/4). - Contact: a fancy contact form, with map, address, telephone, e-mail and opening hours. Just to give it a bit more content, maybe include a catch phrase like "We're looking forward to meeting you!" or something like that. - Estimate: this is the Most Important page in the website (in Addition to the upper part of the Home page). Basically replicate the estimate for the home box, but maybe with a bit more design or extended, Given this is a single page just for that. - Log in: opens a drop-down with user and password (just placeholder, no log in required yet). Regarding colors, we still do not Have a color scheme, so anything in line With the logo is OK. Many thanks in advance, Martin

All ages and genders

Real Estate

Coded - Design and coding required

5+ page

Sans Serif

Must have
• Blank colored background

```html
<!DOCTYPE html>
<html lang="en">
<head>
<meta charset="utf-8">
<title>Portalia — Building Management Estimates</title>
<link rel="stylesheet" href="https://fonts.googleapis.com/css2?family=Open+Sans:wght@400;600;700&display=swap">
<style>
  :root {
    --orange: #c4580b;
    --dark: #3b3b3b;
    --ink: #222222;
    --muted: #777777;
    --footer-bg: #f6f6f6;
    --line: #e4e4e4;
    --white: #ffffff;
  }
  * { box-sizing: border-box; margin: 0; padding: 0; }
  html, body { width: 838px; height: 1200px; overflow: hidden; }
  body { font-family: "Open Sans", Arial, sans-serif; background: var(--white); color: var(--ink); position: relative; }

  /* Header */
  .site-header { position: absolute; left: 0; top: 0; width: 838px; height: 66px; background: var(--white); }
  .brand { position: absolute; left: 100px; top: 21px; font-size: 19px; font-weight: 700; color: var(--dark); letter-spacing: -0.3px; }
  .main-nav { position: absolute; top: 27px; left: 331px; display: flex; gap: 24px; font-size: 9px; font-weight: 600; color: var(--ink); }
  .main-nav .active { color: var(--orange); }
  .btn-estimate { position: absolute; left: 614px; top: 23px; width: 62px; height: 20px; background: var(--orange); color: var(--white); font-size: 8.5px; font-weight: 700; display: flex; align-items: center; justify-content: center; }
  .login { position: absolute; left: 684px; top: 27px; font-size: 9px; font-weight: 700; display: flex; align-items: center; gap: 4px; }

  /* Hero */
  .hero { position: absolute; left: 0; top: 66px; width: 838px; height: 395px; background: linear-gradient(180deg, #9c9c9c 0%, #6e6e6e 45%, #3e3e3e 80%, #2a2a2a 100%); }
  .hero-title { position: absolute; top: 184px; width: 100%; text-align: center; color: var(--white); font-size: 15px; font-weight: 400; letter-spacing: 0.2px; }
  .estimate-fields { position: absolute; left: 99px; top: 231px; display: flex; gap: 4px; }
  .field { width: 103px; height: 25px; background: var(--white); font-size: 7.5px; color: #b0b0b0; padding: 0 8px; display: flex; align-items: center; justify-content: space-between; }
  .btn-search { position: absolute; left: 342px; top: 284px; width: 154px; height: 30px; background: var(--orange); color: var(--white); font-size: 8px; font-weight: 700; display: flex; align-items: center; justify-content: center; }

  /* Request + video */
  .request-box { position: absolute; left: 101px; top: 493px; width: 254px; height: 223px; background: var(--orange); color: var(--white); }
  .request-box h2 { position: absolute; left: 64px; top: 25px; font-size: 17px; font-weight: 600; line-height: 21px; }
  .request-box svg.doc { position: absolute; left: 15px; top: 20px; }
  .request-box p { position: absolute; left: 15px; top: 83px; width: 210px; font-size: 8.5px; line-height: 14.5px; }
  .email-input { position: absolute; left: 15px; top: 122px; width: 225px; height: 32px; border: 1px solid var(--white); font-size: 7.5px; padding-left: 10px; display: flex; align-items: center; }
  .btn-request { position: absolute; left: 16px; top: 169px; width: 92px; height: 25px; background: var(--dark); font-size: 8px; font-weight: 700; display: flex; align-items: center; justify-content: center; }
  .video { position: absolute; left: 373px; top: 493px; width: 364px; height: 223px; background: linear-gradient(180deg, #6d8299 0%, #8b9bab 45%, #3a4a5c 80%, #242c36 100%); }
  .play { position: absolute; left: 156px; top: 95px; width: 50px; height: 30px; background: rgba(30,30,30,0.85); border-radius: 3px; display: flex; align-items: center; justify-content: center; }

  /* Section cards */
  .card { position: absolute; top: 736px; width: 148px; height: 172px; background: var(--dark); color: var(--white); text-align: center; }
  .card.featured { background: var(--orange); }
  .card svg { position: absolute; left: 50%; top: 30px; transform: translateX(-50%); }
  .card h3 { position: absolute; top: 80px; width: 100%; font-size: 19px; font-weight: 600; }
  .card p { position: absolute; top: 116px; left: 10px; right: 10px; font-size: 8.5px; line-height: 14.5px; }

  /* Footer */
  .site-footer { position: absolute; left: 0; top: 956px; width: 838px; height: 208px; background: var(--footer-bg); }
  .footer-brand { position: absolute; left: 102px; top: 32px; font-size: 19px; font-weight: 700; color: var(--dark); }
  .footer-about { position: absolute; left: 102px; top: 78px; width: 215px; font-size: 8.5px; line-height: 14.5px; color: var(--ink); }
  .btn-more { position: absolute; left: 102px; top: 127px; width: 76px; height: 23px; background: var(--orange); color: var(--white); font-size: 8px; font-weight: 700; display: flex; align-items: center; justify-content: center; }
  .link-col { position: absolute; top: 35px; }
  .link-col h4 { font-size: 11px; font-weight: 600; color: var(--orange); margin-bottom: 24px; }
  .link-col ul { list-style: none; font-size: 8px; color: var(--muted); }
  .link-col li { height: 21.6px; }
  .bottom-bar { position: absolute; left: 0; top: 1164px; width: 838px; height: 36px; background: var(--footer-bg); border-top: 1px solid var(--line); font-size: 8px; color: #555; }
  .copyright { position: absolute; left: 102px; top: 13px; }
  .connect { position: absolute; left: 550px; top: 13px; }
  .socials { position: absolute; left: 637px; top: 9px; display: flex; gap: 3px; }
  .socials span { width: 14px; height: 14px; border: 1px solid #b5b5b5; border-radius: 50%; }
  .socials span:first-child { border-color: var(--orange); }
</style>
</head>
<body>

<header class="site-header">
  <div class="brand">Portalia</div>
  <nav class="main-nav">
    <span class="active">HOME</span><span>SERVICES</span><span>ABOUT</span><span>BLOG</span><span>CONTACT US</span>
  </nav>
  <div class="btn-estimate">ESTIMATE</div>
  <div class="login">
    <svg width="6" height="8" viewBox="0 0 6 8"><rect x="0" y="3.5" width="6" height="4.5" fill="#c4580b"/><path d="M1.3 3.5V2.2a1.7 1.7 0 0 1 3.4 0v1.3" fill="none" stroke="#c4580b" stroke-width="1"/></svg>
    LOGIN
  </div>
</header>

<section class="hero" role="img" aria-label="Black and white photograph of the Madrid skyline with office towers at dusk">
  <h1 class="hero-title">INPUT DATA OF YOUR BUILDING TO GET AN ESTIMATE</h1>
  <div class="estimate-fields">
    <div class="field">Post Code</div>
    <div class="field">No.of Homes</div>
    <div class="field">No.of Garages</div>
    <div class="field">No.of Stores</div>
    <div class="field">Swimming Pool <svg width="7" height="5" viewBox="0 0 7 5"><path d="M1 1l2.5 2.5L6 1" fill="none" stroke="#c4580b" stroke-width="1.4"/></svg></div>
    <div class="field">Concierge <svg width="7" height="5" viewBox="0 0 7 5"><path d="M1 1l2.5 2.5L6 1" fill="none" stroke="#c4580b" stroke-width="1.4"/></svg></div>
  </div>
  <div class="btn-search">SEARCH NOW</div>
</section>

<section class="request-box">
  <svg class="doc" width="42" height="50" viewBox="0 0 42 50">
    <path d="M3 3h24l12 12v32H3z" fill="none" stroke="#fff" stroke-width="3" stroke-linejoin="round"/>
    <path d="M27 3v12h12" fill="none" stroke="#fff" stroke-width="3"/>
    <path d="M10 24h22M10 31h22M10 38h22" stroke="#fff" stroke-width="3"/>
  </svg>
  <h2>Request<br>Estimate</h2>
  <p>Sed ut perspiciatis unde omnis iste natus error sit voluptatem accusantium doloremque</p>
  <div class="email-input">ENTER YOUR E-MAIL ADDRESS</div>
  <div class="btn-request">REQUEST NOW</div>
</section>

<section class="video" role="img" aria-label="Corporate presentation video thumbnail showing modern glass office buildings at dusk">
  <div class="play"><svg width="14" height="14" viewBox="0 0 14 14"><path d="M2 1l11 6-11 6z" fill="#fff"/></svg></div>
</section>

<article class="card featured" style="left:101px">
  <svg width="48" height="42" viewBox="0 0 48 42" fill="#3b3b3b">
    <circle cx="18" cy="24" r="11"/><circle cx="18" cy="24" r="4" fill="#c4580b"/>
    <g stroke="#3b3b3b" stroke-width="5"><path d="M18 8v32M2 24h32M6.7 12.7l22.6 22.6M29.3 12.7L6.7 35.3"/></g>
    <circle cx="38" cy="10" r="6"/><circle cx="38" cy="10" r="2" fill="#c4580b"/>
    <g stroke="#3b3b3b" stroke-width="3"><path d="M38 1v18M29 10h18M31.6 3.6l12.8 12.8M44.4 3.6L31.6 16.4"/></g>
    <circle cx="38" cy="34" r="5"/><circle cx="38" cy="34" r="2" fill="#c4580b"/>
    <g stroke="#3b3b3b" stroke-width="3"><path d="M38 27v14M31 34h14"/></g>
  </svg>
  <h3>Services</h3>
  <p>Sed ut perspiciatis unde omnis iste natus error sit</p>
</article>

<article class="card" style="left:264px">
  <svg width="40" height="34" viewBox="0 0 40 34" fill="#c4580b">
    <path d="M20 2L1 18l3 3 16-13 16 13 3-3-7-6V4h-5v4z"/><path d="M7 20l13-10 13 10v13H24v-9h-8v9H7z"/>
  </svg>
  <h3>About</h3>
  <p>Sed ut perspiciatis unde omnis iste natus error sit</p>
</article>

<article class="card" style="left:426px">
  <svg width="44" height="38" viewBox="0 0 44 38" fill="#c4580b">
    <path d="M4 13h10l20-10v30L14 23H4z"/><rect x="36" y="1" width="5" height="34" rx="2"/>
    <path d="M8 25h7l3 11h-6z"/>
  </svg>
  <h3>Blog</h3>
  <p>Sed ut perspiciatis unde omnis iste natus error sit</p>
</article>

<article class="card" style="left:590px">
  <svg width="36" height="36" viewBox="0 0 36 36" fill="#c4580b">
    <path d="M8 2l6 8-4 4c2 5 6 9 11 11l4-4 8 6-4 6C17 33 3 19 2 8z"/>
  </svg>
  <h3>Contact</h3>
  <p>Sed ut perspiciatis unde omnis iste natus error sit</p>
</article>

<footer class="site-footer">
  <div class="footer-brand">Portalia</div>
  <p class="footer-about">Sed ut perspiciatis unde omnis iste natus error sit voluptatem accusantium doloremque laudantium, totam rem aperiam, eaque ipsa quae</p>
  <div class="btn-more">READ MORE</div>
  <div class="link-col" style="left:341px">
    <h4>QUICK LINKS</h4>
    <ul><li>HOME</li><li>SERVICES</li><li>ABOUT</li><li>BLOG</li><li>CONTACT US</li></ul>
  </div>
  <div class="link-col" style="left:470px">
    <h4>OTHER LINKS</h4>
    <ul><li>PRIVACY POLICY</li><li>TERMS OF SERVICE</li><li>LEGAL</li><li>DISCLAIMER</li></ul>
  </div>
  <div class="link-col" style="left:589px">
    <h4>SERVICES</h4>
    <ul><li>ADMINISTRATION</li><li>CONSULTING</li><li>MEDIATION</li></ul>
  </div>
</footer>

<div class="bottom-bar">
  <span class="copyright">© 2016 COMPANY NAME &nbsp;|&nbsp; ALL RIGHTS RESERVED</span>
  <span class="connect">CONNECT WITH US</span>
  <div class="socials" aria-label="Social network links"><span></span><span></span><span></span><span></span><span></span><span></span></div>
</div>

</body>
</html>
```